BrivaLOOM Web Design Project

We would like a website design to go with the new logo. They want something to model this site: http://www.harlenpoxby.com
Using the blue (#3366FF) and green (#33CC33). Like the bight colors in the top half of the home page. Must have a mini form on the interior pages.
Also like this site for inspiration:
http://www.daskelfinhaus.com/
Industry/Entity Type
Interior
Requirements
Must have
- Must fit the brief you had from before.
Must have a mini form
Should not have
- Doesn't have to have to pop up navigation over the slider on the home page.

```html
<!DOCTYPE html>
<html lang="en">
<head>
<meta charset="utf-8">
<title>BrivaLOOM — Who We Are</title>
<link rel="stylesheet" href="https://fonts.googleapis.com/css2?family=Montserrat:wght@400;500;600;700&family=Orbitron:wght@500;600&display=swap">
<style>
  :root {
    --brand-blue: #3366ff;
    --brand-blue-light: #5580ff;
    --brand-green: #33cc33;
    --cta-green-top: #22e022;
    --cta-green-bottom: #10a810;
    --ink: #555b62;
    --logo-grey: #666a70;
    --paper: #ffffff;
    --paper-shade: #eef0f2;
    --field-border: #9bb3ff;
    --field-text: #4a4f55;
    --footer-text: #3a3d42;
  }
  * { box-sizing: border-box; margin: 0; padding: 0; }
  html, body { width: 1108px; height: 1200px; overflow: hidden; }
  body {
    position: relative;
    font-family: "Montserrat", sans-serif;
    background: linear-gradient(160deg, var(--paper) 0%, #f6f7f8 45%, var(--paper) 100%);
  }
  .page { position: absolute; inset: 0; width: 1108px; height: 1200px; overflow: hidden; }

  .backdrop { position: absolute; left: 0; top: 0; width: 1108px; height: 1200px; }

  .brand {
    position: absolute; left: 71px; top: 36px;
    display: flex; align-items: center; gap: 14px;
    font-family: "Montserrat", sans-serif; font-weight: 500;
    font-size: 58px; letter-spacing: -1px; color: var(--logo-grey);
  }
  .brand-dot { width: 22px; height: 22px; border-radius: 50%; background: var(--brand-blue); }

  .main-nav { position: absolute; left: 71px; top: 133px; display: flex; gap: 26px; }
  .main-nav a {
    font-weight: 700; font-size: 16.5px; letter-spacing: 0.6px;
    color: var(--brand-blue); text-decoration: none; text-transform: uppercase;
  }

  .hero-title { position: absolute; left: 68px; top: 178px; }
  .hero-title text { font-family: "Orbitron", sans-serif; font-weight: 500; }
  .hero-sub { position: absolute; left: 70px; top: 277px; }
  .hero-sub text { font-family: "Orbitron", sans-serif; font-weight: 500; }

  .section-title {
    position: absolute; left: 71px; top: 361px;
    color: var(--paper); font-weight: 700; font-size: 26px; letter-spacing: 0.3px;
  }
  .team-photo {
    position: absolute; left: 71px; top: 403px; width: 625px; height: 260px;
    background: linear-gradient(120deg, #c9d3dc 0%, #eef1f4 35%, #9aa6b2 60%, #dfe5ea 100%);
  }
  .body-copy {
    position: absolute; left: 71px; top: 676px; width: 627px;
    color: var(--paper); font-size: 15.6px; line-height: 18.8px; text-align: justify;
  }
  .body-copy p + p { margin-top: 19px; }
  .body-copy p.spaced { margin-top: 38px; }

  .quote-tab {
    position: absolute; left: 696px; top: 307px; width: 352px; height: 60px;
    background: var(--brand-blue); border-radius: 5px 5px 0 0;
    display: flex; align-items: center; padding-left: 22px; gap: 10px;
    color: var(--paper); font-weight: 700; font-size: 16.5px; letter-spacing: 0.3px;
  }
  .quote-form { position: absolute; left: 718px; top: 398px; width: 310px; }
  .field {
    height: 43px; margin-bottom: 14px;
    background: var(--paper); border: 3px solid var(--field-border); border-radius: 4px;
    display: flex; align-items: center; gap: 10px; padding-left: 9px;
    font-size: 16.5px; color: var(--field-text);
  }
  .field svg { flex: none; }
  .field.select { position: relative; }
  .select-arrows {
    position: absolute; right: 0; top: 0; width: 38px; height: 37px;
    background: linear-gradient(#5a5d62, #2f3236);
    display: flex; align-items: center; justify-content: center;
  }
  .quote-button {
    margin-top: 9px; height: 42px; width: 310px;
    border-radius: 4px; border-bottom: 3px solid #0b7f0b;
    background: linear-gradient(var(--cta-green-top), var(--cta-green-bottom));
    color: var(--paper); font-weight: 700; font-size: 16.5px; letter-spacing: 0.5px;
    display: flex; align-items: center; justify-content: center;
  }
  .contact-card { position: absolute; left: 718px; top: 691px; width: 310px; height: 318px; }
  .contact-text {
    position: absolute; left: 20px; top: 21px;
    color: var(--paper); font-size: 16.2px; line-height: 18.8px;
  }
  .contact-text strong { display: block; font-weight: 700; margin-bottom: 11px; }
  .contact-text p + p { margin-top: 19px; }

  .site-footer {
    position: absolute; left: 0; top: 1121px; width: 1108px; height: 79px;
    background: linear-gradient(var(--paper-shade), var(--paper));
  }
  .legal {
    position: absolute; left: 71px; top: 28px;
    font-size: 13px; letter-spacing: 0.4px; color: var(--footer-text); text-transform: uppercase;
  }
  .legal a { color: var(--brand-blue); text-decoration: none; }
  .legal .sep { margin: 0 6px; }
  .footer-brand {
    position: absolute; right: 72px; top: 14px;
    display: flex; align-items: center; gap: 8px;
    font-weight: 500; font-size: 30px; letter-spacing: -0.5px; color: var(--logo-grey);
  }
  .footer-brand .brand-dot { width: 12px; height: 12px; }
</style>
</head>
<body>
<div class="page">

  <svg class="backdrop" width="1108" height="1200" viewBox="0 0 1108 1200" aria-hidden="true">
    <polygon points="0,355 1108,343 1108,1121 0,1121" fill="var(--brand-blue)"/>
    <polygon points="0,355 1108,343 1108,355 0,388" fill="var(--brand-green)"/>
  </svg>

  <header>
    <div class="brand"><span>BrivaLOOM</span><span class="brand-dot"></span></div>
    <nav class="main-nav">
      <a href="#">Who We Are</a>
      <a href="#">What We Do</a>
      <a href="#">Community</a>
      <a href="#">Careers</a>
      <a href="#">Contact</a>
    </nav>
    <svg class="hero-title" width="630" height="100" viewBox="0 0 630 100">
      <text x="0" y="84" font-size="92" fill="var(--brand-green)" textLength="624" lengthAdjust="spacingAndGlyphs">Communicating</text>
    </svg>
    <svg class="hero-sub" width="360" height="32" viewBox="0 0 360 32">
      <text x="0" y="25" font-size="24" fill="var(--ink)" textLength="346" lengthAdjust="spacingAndGlyphs">Enterprise Technology clients.</text>
    </svg>
  </header>

  <main>
    <h2 class="section-title">Who We Are</h2>
    <div class="team-photo" role="img" aria-label="Business team meeting around a conference table"></div>
    <div class="body-copy">
      <p>Lorem ipsum dolor sit amet, consectetur adipiscing elit. Nunc eu massa sem, venenatis adipiscing nulla. Sed tempor posuere orci sit amet gravida. Aenean nisi augue, bibendum in ornare eget, volutpat porta sapien. Suspendisse viverra sagittis arcu, euismod luctus dui euismod sed. Aenean tincidunt, justo blandit interdum tincidunt, erat odio sagittis orci, pulvinar ullamcorper neque diam volutpat augue. Suspendisse at lobortis felis. Nunc aliquam risus quis augue gravida porta. Maecenas erat tellus, pretium consectetur semper ut, placerat nec velit.</p>
      <p>Morbi vel nibh ut leo ullamcorper hendrerit sed id augue. Aenean non leo justo. Cum sociis natoque penatibus et magnis dis parturient montes, nascetur ridiculus mus. Maecenas erat tellus, pretium consectetur semper ut, placerat nec velit. Morbi luctus fermentum libero eu gravida. Quisque sodales erat non urna sodales convallis sit amet vitae leo. Ut et elit ac arcu convallis vestibulum non non ligulla ultrices lacus.</p>
      <p class="spaced">Condimentum mauris mattis convallis. Sed posuere lacus eget purus eleifend quis rutrum elit vehicula. Morbi vel nibh ut leo ullamcorper hendrerit sed id augue. Aenean non leo justo. Cum sociis natoque penatibus et magnis dis parturient montes, nascetur ridiculus mus. Maecenas erat tellus, pretium consectetur semper ut, placerat nec velit.</p>
    </div>
  </main>

  <aside>
    <div class="quote-tab">
      <svg width="32" height="32" viewBox="0 0 32 32" aria-hidden="true">
        <circle cx="16" cy="16" r="14" fill="none" stroke="#fff" stroke-width="2.5"/>
        <path d="M10 22 l2-6 8-8 4 4 -8 8z" fill="#fff"/>
      </svg>
      <span>FREE QUOTE</span>
    </div>

    <form class="quote-form">
      <div class="field">
        <svg width="20" height="20" viewBox="0 0 20 20" aria-hidden="true"><circle cx="10" cy="6" r="4.5" fill="#9a9ea4"/><path d="M2 19 c0-6 4-8 8-8 s8 2 8 8z" fill="#9a9ea4"/></svg>
        <span>name</span>
      </div>
      <div class="field">
        <svg width="20" height="20" viewBox="0 0 20 20" aria-hidden="true"><path d="M4 2 l4 0 1 5 -2 2 c1 2 2 3 4 4 l2-2 5 1 0 4 c-1 2-3 2-4 2 C8 17 3 12 2 6 c0-2 0-3 2-4z" fill="#9a9ea4"/></svg>
        <span>telephone</span>
      </div>
      <div class="field">
        <svg width="20" height="20" viewBox="0 0 20 20" aria-hidden="true"><rect x="1" y="4" width="18" height="12" fill="#9a9ea4"/><path d="M1 4 l9 7 9-7" fill="none" stroke="#fff" stroke-width="1.5"/></svg>
        <span>email</span>
      </div>
      <div class="field select">
        <svg width="20" height="20" viewBox="0 0 20 20" aria-hidden="true"><path d="M11 1 l8 8 -2 1 -2-1 -3 3 1 4 -1 1 -4-4 -5 6 -1-1 6-5 -4-4 1-1 4 1 3-3 -1-2z" fill="#9a9ea4"/></svg>
        <span>interested in</span>
        <span class="select-arrows">
          <svg width="12" height="18" viewBox="0 0 12 18" aria-hidden="true"><path d="M6 1 l5 6 H1z M6 17 l5-6 H1z" fill="#fff"/></svg>
        </span>
      </div>
      <div class="quote-button">GET A FREE QUOTE</div>
    </form>

    <div class="contact-card">
      <svg width="310" height="318" viewBox="0 0 310 318" style="position:absolute;left:0;top:0" aria-hidden="true">
        <polygon points="0,0 310,0 310,296 0,318" fill="var(--brand-blue-light)"/>
      </svg>
      <div class="contact-text">
        <strong>BrivaLoom Inc</strong>
        <p>Calder Plaza, 14th Floor<br>Suite 1400, New York<br>New York 10027, USA</p>
        <p>Tel: +1 555 014 2290<br>Fax: +1 555 014 2291<br>Email: hello@brivaloom.com</p>
      </div>
    </div>
  </aside>

  <footer class="site-footer">
    <p class="legal">Copyright © 2012 BrivaLOOM. All rights reserved.<span class="sep">|</span><a href="#">Terms of Use</a></p>
    <div class="footer-brand"><span>BrivaLOOM</span><span class="brand-dot"></span></div>
  </footer>

</div>
</body>
</html>
```